Business Card Design

New business card design

Target Market(s)

Residential & Commercial Property Managers

Industry/Entity Type

Plumbing Services

Contact Information for Business Card

Name - Owen Tredgold, title - Director, Phone Number - 0431 862 507, email - owen@rvb-plumbing.com.au, Company ABN - 73 215 904 386,

Font styles to use
Sans Serif

Colors
0054AA
0677BA
7BADD7
CADEEF
E8F1F8

```html
<!DOCTYPE html>
<html lang="en">
<head>
<meta charset="utf-8">
<title>RVB Plumbing Services – Business Card</title>
<link href="https://fonts.googleapis.com/css2?family=Montserrat:wght@300;400;500;700&display=swap" rel="stylesheet">
<style>
  :root {
    --page: #0d0d0e;
    --card: #1b1b1c;
    --card-curve: #202021;
    --wordmark: #2b3540;
    --tagline: #6f6354;
    --blue: #0aa6e8;
    --muted: #7c7264;
    --rule: #4a433a;
  }
  * { box-sizing: border-box; margin: 0; padding: 0; }
  html, body { width: 1200px; height: 1200px; overflow: hidden; background: var(--page); }
  body { font-family: "Montserrat", sans-serif; position: relative; }

  .card {
    position: absolute;
    left: 220px;
    width: 760px;
    height: 434px;
    background: var(--card);
    border-radius: 22px;
    overflow: hidden;
  }
  .card--front { top: 110px; }
  .card--back { top: 640px; }

  .front-curve { position: absolute; inset: 0; }

  .brand {
    position: absolute;
    display: flex;
    align-items: center;
    gap: 14px;
  }
  .brand__dot {
    width: 22px; height: 22px;
    border-radius: 50%;
    background: var(--blue);
    flex: none;
  }
  .brand__name {
    font-weight: 300;
    color: var(--wordmark);
    line-height: 1.05;
    letter-spacing: 0.04em;
    text-transform: lowercase;
  }
  .card--front .brand { left: 200px; top: 150px; }
  .card--front .brand__name { font-size: 54px; }
  .card--back .brand { right: 60px; top: 56px; }
  .card--back .brand__name { font-size: 36px; }
  .card--back .brand__dot { width: 16px; height: 16px; }

  .contact {
    position: absolute;
    left: 60px;
    bottom: 48px;
    width: 640px;
  }
  .contact__name {
    font-weight: 700;
    font-size: 26px;
    color: var(--blue);
    text-transform: uppercase;
    letter-spacing: 0.01em;
  }
  .contact__title {
    font-size: 21px;
    font-weight: 400;
    color: var(--muted);
    margin-top: 2px;
  }
  .contact__rule {
    height: 1px;
    background: var(--rule);
    margin: 14px 0 14px;
  }
  .contact__abn {
    position: absolute;
    right: 0;
    top: 40px;
    font-size: 19px;
    font-weight: 500;
    color: var(--muted);
  }
  .contact__line {
    display: flex;
    align-items: center;
    gap: 12px;
    font-size: 19px;
    color: var(--muted);
    margin-top: 6px;
  }
  .contact__line svg { width: 18px; height: 18px; flex: none; }

  .band {
    position: absolute;
    left: 0; right: 0; bottom: 0;
    height: 12px;
    background: var(--blue);
  }
</style>
</head>
<body>

  <section class="card card--front" aria-label="Card front">
    <svg class="front-curve" viewBox="0 0 760 434" aria-hidden="true">
      <path d="M0 0 H150 C330 60 380 260 300 434 H0 Z" fill="var(--card-curve)"/>
    </svg>
    <div class="brand">
      <span class="brand__dot"></span>
      <span class="brand__name">rvb plumbing services</span>
    </div>
  </section>

  <section class="card card--back" aria-label="Card back">
    <div class="brand">
      <span class="brand__dot"></span>
      <span class="brand__name">rvb plumbing services</span>
    </div>

    <div class="contact">
      <div class="contact__abn">ABN: 73 215 904 386</div>
      <div class="contact__name">Owen Tredgold</div>
      <div class="contact__title">Director</div>
      <div class="contact__rule"></div>
      <div class="contact__line">
        <svg viewBox="0 0 24 24" aria-hidden="true"><path fill="var(--blue)" d="M6.6 10.8a15 15 0 0 0 6.6 6.6l2.2-2.2c.3-.3.7-.4 1-.2 1.1.4 2.3.6 3.6.6.6 0 1 .4 1 1V20c0 .6-.4 1-1 1A17 17 0 0 1 3 4c0-.6.4-1 1-1h3.5c.6 0 1 .4 1 1 0 1.3.2 2.5.6 3.6.1.3 0 .7-.2 1z"/></svg>
        <span>0431 862 507</span>
      </div>
      <div class="contact__line">
        <svg viewBox="0 0 24 24" aria-hidden="true"><rect x="2" y="5" width="20" height="14" rx="2" fill="var(--blue)"/><path d="M3 6l9 7 9-7" fill="none" stroke="var(--card)" stroke-width="1.8"/></svg>
        <span>owen@rvb-plumbing.com.au</span>
      </div>
    </div>

    <div class="band"></div>
  </section>

</body>
</html>
```